International Property Consultancy

Detailed Wireframe and info document attached.

Brief Overview:

I need a dynamic and well designed website that is easy to use and understand. It has to be unique and different to generic templates that most websites seem to be these days. PLEASE NO GENERIC TEMPLATES FROM THE INTERNET.

Our business has 10 years experience working on struggling international developments that we then work in-house for to turn around and brings bout success. We stay within a project often for long periods of time until success is achieved. We are unique in our approach and completely different to the standard routes to market for many developments. The site is for developers to see what we have done in regards to previous projects, as such we want to incorporate video into this site with a strong design aesthetic. There will be videos of the past projects we have worked on, which will act as case studies.

I like very simple but punchy websites, that people can navigate and understand very easily. Also a big fan of unique and well thought out design aesthetic.

Initial Site layout thoughts:

1) Homepage:
2) About Us
3) What we've done / Work
This part has the projects we have worked on (France, Portugal, London, Morocco). Each one will have some video content and photo images, but also would be good to have a succinct way to mention what we did and the successes in a clever and punchy way.

4) Contact Us

* This is just a guideline. Would be open to input and creative direction on your own part.

*More details and websites we like can be seen in the brief doc attached.

PLEASE VIEW THE WIREFRAME WORD DOC ATTACHED.

Here there are also some more examples to help:

Here are just a few examples of websites and what I like about them:

- www.velmorit.com (clean, nice geometric design aesthetic, good animation when loading and changing pages well thought out all though also coulee be considered a bit dull and basic after the initial homepage slide)
- https://www.farbridgeloop.net (Clean site, quite clinical, lacks video content and doesn't engage greatly).
- https://quiltmarsh.com (minimal, and like how it mixes the design aesthetic more with video and photo content)

- https://www.theamberotter.com (like the layout of this and how it displays the projects and work section)

- https://drov.com (Good use of video content)

- https://crafthalo.studio (minimal to the point and mixes design with video and animation etc...)

Here is another couple of cool websites that may help give you some direction: https://tidewellgroup.com www.drov.com

Hi there, One of the things I thought would be good on the homepage is to add the logo with a 'digital landscape' before flicking down into a slide with video content of the projects... Just an idea but have posted some pics in the brief. We would get this animated for the site. But if you have better ideas, please do run with them. Thanks,

Target Market(s)

Property developers

Number of Pages Required

4 page

Font styles to use
Other font styles liked:
• Read brief

Requirements
Must have
• Needs to be clean, dynamic and easy to follow on desktop and mobile. We will use it as a kind of portfolio website so will need to embed video of past projects we have worked on.

Read brief in docs.
Nice to have
• Clean
Should not have
• Not be another generic template website.
Not have random property stock photos. (We are not a property agency).

```html
<!DOCTYPE html>
<html lang="en">
<head>
<meta charset="utf-8">
<title>Meridane — International Property Developments</title>
<link rel="stylesheet" href="https://fonts.googleapis.com/css2?family=Comfortaa:wght@600;700&family=Lato:wght@400;700&display=swap">
<style>
:root{
  --ink:#0f1d27;
  --text:#1b1b1b;
  --muted:#5b5b5b;
  --peach:#f8dfd6;
  --accent:#f0a99a;
  --white:#ffffff;
  --rule:#e6e6e6;
}
*{margin:0;padding:0;box-sizing:border-box}
html,body{width:1200px;height:2928px;overflow:hidden;background:var(--white)}
body{position:relative;font-family:"Lato",sans-serif;color:var(--text)}
.abs{position:absolute}
.display{font-family:"Comfortaa",sans-serif;font-weight:700;color:var(--ink);letter-spacing:.5px}

/* header */
.brand{left:98px;top:30px;font-size:34px}
.nav{left:322px;top:42px;display:flex;gap:20px;font-size:14.5px;font-weight:700;color:var(--ink)}
.nav a{color:inherit;text-decoration:none;position:relative}
.nav a.active::before{content:"";position:absolute;left:50%;top:-12px;width:7px;height:7px;margin-left:-3px;border-radius:50%;background:var(--accent)}
.btn{display:flex;align-items:center;justify-content:center;gap:10px;border-radius:26px;font-size:14px;font-weight:700;text-decoration:none}
.btn-dark{background:var(--ink);color:var(--white)}
.btn-peach{background:var(--peach);color:var(--ink)}
.btn svg{width:14px;height:14px}

/* hero */
.hero-title{left:110px;top:128px;font-size:58px}
.hero-sub{left:113px;top:208px;font-size:27px;color:var(--text)}
.hero-band{left:0;top:240px;width:1200px;height:590px;
  background:radial-gradient(ellipse 70% 30% at 50% 45%,rgba(170,200,225,.45),rgba(255,255,255,0) 70%),
             linear-gradient(180deg,#fff 0%,#eef4f9 35%,#e7f0f7 55%,#fff 100%)}
.hero-mark{left:0;width:1200px;top:400px;text-align:center;font-size:88px}
.play{left:567px;top:533px}
.scroll{left:1132px;top:490px;writing-mode:vertical-rl;transform:rotate(180deg);font-size:13px;font-weight:700;color:var(--ink)}
.scroll-arrow{left:1138px;top:555px}

/* projects */
.section-title{font-size:52px}
.projects-title{left:0;width:1200px;top:760px;text-align:center}
.card{top:880px;height:427px;width:656px;overflow:hidden}
.card span{position:absolute;left:0;right:0;bottom:72px;text-align:center;font-family:"Comfortaa",sans-serif;font-weight:700;font-size:44px;color:var(--white)}
.card-fr{left:-456px;background:linear-gradient(180deg,#9fb2b4 0%,#b9bfb6 45%,#6c6558 100%)}
.card-pt{left:272px;background:linear-gradient(180deg,#4a6f9c 0%,#8ea6b9 30%,#c9c2b4 45%,#3d8ea6 65%,#2b7f95 100%)}
.card-ma{left:1000px;background:linear-gradient(180deg,#8c5a3c 0%,#d59a5c 25%,#7a5238 55%,#3b2b22 100%)}
.card-ma span{text-align:left;left:122px}
.arrow-btn{top:1361px;width:42px;height:39px;border:1px solid #cfcfcf;display:flex;align-items:center;justify-content:center;background:var(--white)}

/* about */
.about-title{left:108px;top:1505px}
.about-copy{left:114px;top:1588px;width:540px;font-size:17.5px;line-height:30px;color:var(--muted)}
.stat-num{left:822px;font-family:"Lato",sans-serif;font-weight:700;font-size:72px;color:var(--text);line-height:1}
.stat-label{left:824px;font-size:14px;font-weight:700;color:#444}
.read-more{left:114px;top:1884px;width:164px;height:50px}

.photo{width:289px;height:356px}

/* footer */
.foot-col{top:2560px}
.foot-col h4{font-size:14.5px;font-weight:700;color:var(--ink);margin-bottom:22px}
.foot-col li{list-style:none;font-size:15px;color:var(--muted);height:34.3px;display:flex;align-items:flex-start;gap:14px}
.foot-col li::before{content:"»";color:var(--ink);font-size:15px;line-height:1}
.foot-brand{left:705px;top:2570px;font-size:84px}
.social{top:2689px;width:38px;height:38px;border:2px solid var(--ink);border-radius:50%}
.rule{left:0;top:2808px;width:1200px;height:1px;background:var(--rule)}
.copy{left:762px;top:2862px;font-size:15px;color:var(--muted)}
</style>
</head>
<body>

<header>
  <div class="abs display brand">meridane.</div>
  <nav class="abs nav">
    <a class="active" href="#">HOME</a>
    <a href="#">ABOUT US</a>
    <a href="#">RECENT PROJECTS</a>
    <a href="#">CONTACT US</a>
  </nav>
  <a class="abs btn btn-dark" href="#" style="left:763px;top:27px;width:203px;height:47px">CREATE AN ACCOUNT
    <svg viewBox="0 0 16 16"><circle cx="8" cy="8" r="7" fill="none" stroke="#fff" stroke-width="1.6"/><circle cx="8" cy="6.5" r="2.3" fill="#fff"/><path d="M3.8 12.4c1-1.8 2.4-2.5 4.2-2.5s3.2.7 4.2 2.5" fill="#fff"/></svg></a>
  <a class="abs btn btn-peach" href="#" style="left:978px;top:27px;width:124px;height:47px">LOG IN
    <svg viewBox="0 0 16 16"><rect x="3" y="7" width="10" height="8" rx="1" fill="#0f1d27"/><path d="M5 7V5a3 3 0 0 1 6 0v2" fill="none" stroke="#0f1d27" stroke-width="1.8"/></svg></a>
</header>

<section>
  <h1 class="abs display hero-title">we are meridane</h1>
  <p class="abs hero-sub">We Fulfill international Property developments</p>
  <div class="abs hero-band" role="img" aria-label="Soft blue digital wave landscape"></div>
  <div class="abs display hero-mark">meridane.</div>
  <svg class="abs play" width="66" height="66" viewBox="0 0 66 66" aria-label="Play video">
    <circle cx="33" cy="33" r="33" fill="#5f7f8e"/>
    <circle cx="33" cy="33" r="27" fill="#12303c"/>
    <path d="M27 22l16 11-16 11z" fill="#fff"/>
  </svg>
  <div class="abs scroll">SCROLL</div>
  <svg class="abs scroll-arrow" width="12" height="32" viewBox="0 0 12 32"><path d="M6 0v28M1 23l5 6 5-6" fill="none" stroke="#8a8a8a" stroke-width="2"/></svg>
</section>

<section>
  <h2 class="abs display section-title projects-title">recent projects</h2>
  <div class="abs card card-fr" role="img" aria-label="Photo of Paris skyline with tower"><span>France</span></div>
  <div class="abs card card-pt" role="img" aria-label="Photo of Portuguese coastal town and harbour"><span>Portugal Resort</span></div>
  <div class="abs card card-ma" role="img" aria-label="Photo of Moroccan market square at dusk"><span>morocco</span></div>
  <div class="abs arrow-btn" style="left:551px"><svg width="14" height="22" viewBox="0 0 14 22"><path d="M11 2L3 11l8 9" fill="none" stroke="#111" stroke-width="2.2"/></svg></div>
  <div class="abs arrow-btn" style="left:607px"><svg width="14" height="22" viewBox="0 0 14 22"><path d="M3 2l8 9-8 9" fill="none" stroke="#111" stroke-width="2.2"/></svg></div>
</section>

<section>
  <h2 class="abs display section-title about-title">about us</h2>
  <p class="abs about-copy">Meridane is a consultancy company that helps international property<br>developments fulfil<br>their potential. The company has had great success over the last 10<br>years of turning around<br>struggling property developments (often resort and investment) and<br>making them reach<br>their maximum potential. We have completed projects in Portugal,<br>London, France,<br>Morocco, Brazil etc…</p>
  <div class="abs stat-num" style="top:1606px">30+</div>
  <div class="abs stat-label" style="top:1687px">MEMBERS</div>
  <div class="abs stat-num" style="top:1743px">10</div>
  <div class="abs stat-label" style="top:1824px">YEARS IN BUSINESS</div>
  <a class="abs btn btn-dark read-more" href="#">READ MORE
    <svg viewBox="0 0 16 16"><circle cx="8" cy="8" r="7" fill="#fff"/><path d="M6.5 4.5L10 8l-3.5 3.5" fill="none" stroke="#0f1d27" stroke-width="2"/></svg></a>

  <div class="abs photo" style="left:0;top:2026px;background:linear-gradient(160deg,#c9c4bb,#8a7d6e 60%,#b89c78)" role="img" aria-label="Photo of a team working together at a laptop"></div>
  <div class="abs photo" style="left:303px;top:2092px;background:linear-gradient(160deg,#d8b48c,#c08a5a 55%,#8f6a4c)" role="img" aria-label="Photo of a laptop and calculator on a wooden desk"></div>
  <div class="abs photo" style="left:608px;top:2026px;background:linear-gradient(160deg,#b9c4c8,#5e7a93 50%,#7c6a5a)" role="img" aria-label="Photo of colleagues smiling around a laptop"></div>
  <div class="abs photo" style="left:911px;top:2092px;background:linear-gradient(160deg,#3f5a3a,#a8b0a6 50%,#d9c4a4)" role="img" aria-label="Photo of a woman working on a laptop in a café"></div>
</section>

<footer>
  <div class="abs foot-col" style="left:116px">
    <h4>QUICK LINKS</h4>
    <ul><li>Home</li><li>About us</li><li>Recent Projects</li><li>Reviews</li><li>Contact us</li></ul>
  </div>
  <div class="abs foot-col" style="left:373px">
    <h4>OTHER LINKS</h4>
    <ul><li>FAQ</li><li>Privacy Policy</li><li>Terms &amp; Conditions</li><li>Help Service</li><li>Contact us</li></ul>
  </div>
  <div class="abs display foot-brand">meridane.</div>
  <div class="abs social" style="left:910px" aria-label="Professional network"></div>
  <div class="abs social" style="left:956px" aria-label="Photo network"></div>
  <div class="abs social" style="left:1000px" aria-label="Microblog"></div>
  <div class="abs social" style="left:1045px" aria-label="Social network"></div>

  <div class="abs rule"></div>
  <a class="abs btn btn-dark" href="#" style="left:112px;top:2849px;width:203px;height:46px">CREATE AN ACCOUNT
    <svg viewBox="0 0 16 16"><circle cx="8" cy="8" r="7" fill="none" stroke="#fff" stroke-width="1.6"/><circle cx="8" cy="6.5" r="2.3" fill="#fff"/><path d="M3.8 12.4c1-1.8 2.4-2.5 4.2-2.5s3.2.7 4.2 2.5" fill="#fff"/></svg></a>
  <a class="abs btn btn-peach" href="#" style="left:327px;top:2849px;width:124px;height:46px">LOG IN
    <svg viewBox="0 0 16 16"><rect x="3" y="7" width="10" height="8" rx="1" fill="#0f1d27"/><path d="M5 7V5a3 3 0 0 1 6 0v2" fill="none" stroke="#0f1d27" stroke-width="1.8"/></svg></a>
  <p class="abs copy">© 2020 Meridane. All Rights Reserved</p>
</footer>

</body>
</html>
```